Harborline Open Cinema Gathering 20th Annual Poster

September 2017 will to the 20th Annual Harborline Open Cinema Gathering. We have a new logo and need a new modern stylish poster designed. One that shows creativity, imagination, style and class. Think outside the box. Modern and new.

Dates are: September 7th - 13th 2017

Our tagline:
"Something for Everyone from Around the World"

Target Market(s)

film festival goings - 35 - 70 age range - 58% female 42% males - movie lovers - movie goers

Industry/Entity Type

Movie

Font styles to use
Script

Requirements
Must have
• modern style celebrating 20 years - cool design - chic and stylish - upscale - high society - think Abstract
Nice to have
• thinking outside the box - not just simple film reel - think Abstract! Not just your standard film items. Creative in your idea and design
Should not have
• no CLIP ART

```html
<!DOCTYPE html>
<html lang="en">
<head>
<meta charset="utf-8">
<title>Harborline Open Cinema Gathering – 20th Annual Poster</title>
<link rel="stylesheet" href="https://fonts.googleapis.com/css2?family=Lato:wght@400;700&display=swap">
<style>
  :root {
    --backdrop: #a9a9a9;
    --night-top: #050505;
    --night-bottom: #141414;
    --ink-white: #f4f4f4;
    --accent-green: #7cbc3c;
    --globe-blue: #1585bb;
  }
  * { margin: 0; padding: 0; box-sizing: border-box; }
  html, body {
    width: 1200px;
    height: 1200px;
    overflow: hidden;
    background: var(--backdrop);
    font-family: "Lato", sans-serif;
    font-weight: 700;
  }
  .poster {
    position: absolute;
    left: 200px;
    top: 35px;
    width: 800px;
    height: 1130px;
    overflow: hidden;
    background: linear-gradient(to bottom, var(--night-top), var(--night-bottom));
  }
  .poster-art {
    position: absolute;
    inset: 0;
    width: 800px;
    height: 1130px;
  }
  .brand {
    position: absolute;
    left: 0;
    width: 800px;
    top: 76px;
    text-align: center;
    color: var(--ink-white);
  }
  .brand-mark {
    display: block;
    width: 28px;
    height: 28px;
    margin: 0 auto 6px;
    border-radius: 50%;
    background: var(--accent-green);
  }
  .brand-name {
    font-size: 34px;
    letter-spacing: 3px;
    line-height: 1;
  }
  .brand-full-name {
    display: inline-block;
    margin-top: 4px;
    padding-top: 3px;
    border-top: 1px solid var(--accent-green);
    font-size: 7px;
    letter-spacing: 0.4px;
    line-height: 1;
  }
  .tagline {
    position: absolute;
    font-size: 20px;
    line-height: 21px;
    color: var(--ink-white);
    text-transform: uppercase;
  }
  .tagline .highlight { color: var(--accent-green); }
  .tagline-left {
    right: 411px;
    top: 365px;
    text-align: right;
  }
  .tagline-right {
    left: 408px;
    top: 413px;
    text-align: left;
  }
  .event-details {
    position: absolute;
    left: 0;
    width: 800px;
    top: 975px;
    text-align: center;
    color: var(--ink-white);
    text-transform: uppercase;
  }
  .event-edition {
    font-size: 20px;
    letter-spacing: 4px;
    line-height: 1.2;
  }
  .event-dates {
    margin-top: 8px;
    font-size: 16px;
    font-weight: 400;
    letter-spacing: 3px;
    line-height: 1.2;
  }
</style>
</head>
<body>
  <main class="poster">
    <svg class="poster-art" viewBox="0 0 800 1130">
      <line class="guide-line" x1="400" y1="0" x2="400" y2="66"
            stroke="var(--ink-white)" stroke-width="3" stroke-dasharray="15 8"/>
      <line class="guide-line" x1="400" y1="172" x2="400" y2="708"
            stroke="var(--ink-white)" stroke-width="3" stroke-dasharray="15 8"/>
      <circle class="rising-reel" cx="400" cy="838" r="130" fill="var(--ink-white)"
              role="img" aria-label="Film reel rising over the globe horizon"/>
      <path class="globe-horizon"
            d="M0 906 Q400 760 800 906 L800 1130 L0 1130 Z"
            fill="var(--globe-blue)"/>
    </svg>

    <header class="brand">
      <span class="brand-mark"></span>
      <div class="brand-name">HOCG</div>
      <div class="brand-full-name">HARBORLINE OPEN CINEMA GATHERING</div>
    </header>

    <p class="tagline tagline-left">Something<br>For <span class="highlight">Everyone</span></p>
    <p class="tagline tagline-right">From Around<br><span class="highlight">The World</span></p>

    <section class="event-details">
      <p class="event-edition">20th Annual</p>
      <p class="event-dates">September 7 – 13, 2017</p>
    </section>
  </main>
</body>
</html>
```